Kestrel Gardenworks Flyer

I would like to purchase a customized version of a design you have previously submitted - https://www.artbidhub-example.com/design/8374215
Hello,
I like this design a lot. I would change the bullet points to;
- Landscape Design & Construction
- Paver Patio/path installations
- Retaining wall installations
- Pergola Installations
- Grading
- All Hardscape construction
- Drainage specialist
- Yard Maintenance plans
- Mulch & Pine needles
- Bloomin' Great Service!
In the yellow star part - "Mention this flyer for a 10% discount!"
Our logo is attached
Phone number - 7045182094
email - kestrelgardenworks@mailbox-example.com
website - www.kestrelgardenworks-example.com
Target Market(s)
Residential homes in Charlotte, North Carolina
Industry/Entity Type
Landscaping
Look and feel

```html
<!DOCTYPE html>
<html lang="en">
<head>
<meta charset="utf-8">
<title>Kestrel Gardenworks Flyer</title>
<link href="https://fonts.googleapis.com/css2?family=Montserrat:wght@500;600;700;800;900&display=swap" rel="stylesheet">
<style>
  :root {
    --paper: #f0f0ef;
    --paper-shade: #dcdcdb;
    --leaf: #3f8f1c;
    --leaf-bright: #5aab22;
    --leaf-deep: #2e6a1e;
    --field: #326c22;
    --soil: #5b3518;
    --soil-dark: #46270f;
    --sun: #ffe21f;
    --ink: #151515;
    --white: #ffffff;
  }
  * { box-sizing: border-box; margin: 0; padding: 0; }
  html, body { width: 800px; height: 1200px; overflow: hidden; background: var(--white); }
  body { font-family: "Montserrat", sans-serif; }
  .flyer { position: relative; width: 800px; height: 1200px; overflow: hidden; background: var(--paper); }
  .flyer-shapes { position: absolute; inset: 0; width: 800px; height: 1200px; }

  .brand { position: absolute; left: 58px; top: 92px; display: flex; align-items: center; gap: 10px; }
  .brand-dot { width: 22px; height: 22px; border-radius: 50%; background: var(--soil); }
  .brand-name { font-weight: 800; font-size: 23px; color: var(--soil); letter-spacing: 0.2px; white-space: nowrap; }

  .headline {
    position: absolute; left: 335px; top: 48px; width: 440px; text-align: center;
    font-weight: 900; font-size: 41px; line-height: 62px; color: var(--leaf);
    text-transform: uppercase; letter-spacing: 0.5px;
  }

  .garden-photo { position: absolute; inset: 0; }

  .work-photo {
    position: absolute; border-radius: 50%;
    border: 5px solid #d9dcd6;
    background: radial-gradient(circle at 50% 35%, #b9a58f 0%, #8f8a6e 35%, #6f8e3e 65%, #3f6b27 100%);
  }
  .work-photo.one { left: 318px; top: 716px; width: 204px; height: 204px; }
  .work-photo.two { left: 513px; top: 660px; width: 226px; height: 226px; }

  .services { position: absolute; left: 56px; top: 762px; color: var(--white); }
  .services-title { font-weight: 900; font-size: 24px; letter-spacing: 0.5px; color: var(--leaf-deep);
    -webkit-text-stroke: 1.2px var(--white); text-transform: uppercase; }
  .services-rule { width: 42px; height: 3px; background: var(--white); margin: 4px 0 12px; }
  .services-list { list-style: none; }
  .services-list li { display: flex; align-items: center; gap: 9px; font-weight: 500; font-size: 13.5px; height: 25.7px; white-space: nowrap; }
  .tick { width: 12px; height: 12px; flex: none; }

  .promise {
    position: absolute; left: 320px; top: 973px; width: 262px; height: 76px;
    background: var(--ink); border-radius: 12px; color: var(--white);
    font-weight: 700; font-size: 14px; line-height: 19px; text-align: center;
    display: flex; align-items: center; justify-content: center; padding-right: 24px;
  }

  .discount { position: absolute; left: 557px; top: 870px; width: 196px; height: 196px; }
  .discount-star { position: absolute; inset: 0; width: 196px; height: 196px; }
  .discount-lead { position: absolute; left: 0; right: 0; top: 66px; text-align: center;
    font-weight: 600; font-size: 10.5px; line-height: 13px; color: var(--ink); white-space: nowrap; }
  .discount-value { position: absolute; left: 0; right: 0; top: 82px; text-align: center;
    font-weight: 800; font-size: 48px; line-height: 50px; color: var(--ink); letter-spacing: -3px; }
  .discount-label { position: absolute; left: 0; right: 0; top: 134px; text-align: center;
    font-weight: 600; font-size: 12.5px; color: var(--ink); }

  .contact-tab {
    position: absolute; left: 292px; top: 1078px; width: 220px; height: 44px;
    background: var(--leaf-bright); border: 3px solid #8ccf3e; border-radius: 8px 8px 2px 2px;
    color: var(--white); font-weight: 800; font-size: 23px; letter-spacing: 0.5px;
    display: flex; align-items: center; justify-content: center;
  }

  .contact-line { position: absolute; left: 56px; right: 16px; top: 1143px; display: flex; align-items: center;
    color: var(--white); font-weight: 500; font-size: 12px; white-space: nowrap; }
  .contact-item { display: flex; align-items: center; gap: 7px; }
  .contact-item.phone { width: 118px; }
  .contact-item.email { width: 300px; }
  .contact-icon { width: 12px; height: 12px; flex: none; }
</style>
</head>
<body>
<main class="flyer">

  <svg class="flyer-shapes" viewBox="0 0 800 1200" aria-hidden="true">
    <defs>
      <linearGradient id="paperShade" x1="0" y1="0" x2="1" y2="1">
        <stop offset="0" stop-color="#f4f4f3"/>
        <stop offset="1" stop-color="#e4e4e3"/>
      </linearGradient>
      <linearGradient id="fieldShade" x1="0" y1="0" x2="0" y2="1">
        <stop offset="0" stop-color="#37752a"/>
        <stop offset="1" stop-color="#2c6420"/>
      </linearGradient>
    </defs>
    <rect width="800" height="1200" fill="url(#paperShade)"/>
  </svg>

  <svg class="garden-photo" viewBox="0 0 800 1200" role="img" aria-label="Photograph of a landscaped garden with a large tree, lawn and beds of red, yellow and pink flowers">
    <defs>
      <linearGradient id="gardenTones" x1="0" y1="0" x2="0" y2="1">
        <stop offset="0" stop-color="#2e4f22"/>
        <stop offset="0.35" stop-color="#4f7a2c"/>
        <stop offset="0.55" stop-color="#8a4a2a"/>
        <stop offset="0.7" stop-color="#5f962f"/>
        <stop offset="1" stop-color="#3d6e2a"/>
      </linearGradient>
    </defs>
    <rect x="0" y="240" width="800" height="620" fill="url(#gardenTones)"/>
  </svg>

  <svg class="flyer-shapes" viewBox="0 0 800 1200" aria-hidden="true">
    <path d="M0,222 C170,182 340,205 445,255 C560,312 680,312 800,285 L800,335 C680,352 560,348 440,300 C330,258 170,252 0,268 Z" fill="var(--leaf)"/>
    <path d="M0,268 C170,252 330,258 440,300 C560,348 680,352 800,335 L800,343 C680,360 560,356 440,308 C330,266 170,260 0,276 Z" fill="var(--soil)"/>
    <path d="M0,0 H800 V285 C680,312 560,312 445,255 C340,205 170,182 0,222 Z" fill="url(#paperShade)"/>
    <path d="M0,712 C150,672 300,647 430,662 C560,677 680,782 800,812 L800,832 C680,802 560,697 430,682 C300,667 150,692 0,732 Z" fill="var(--soil)"/>
    <path d="M0,732 C150,692 300,667 430,682 C560,697 680,802 800,832 V1200 H0 Z" fill="url(#fieldShade)"/>
    <path d="M0,1128 C200,1102 500,1092 800,1088" stroke="var(--leaf-bright)" stroke-width="6" fill="none"/>
    <path d="M0,1134 C200,1108 500,1098 800,1094 V1200 H0 Z" fill="var(--soil)"/>
  </svg>

  <div class="brand">
    <span class="brand-dot"></span>
    <span class="brand-name">Kestrel Gardenworks</span>
  </div>

  <h1 class="headline">Give your<br>lawn the<br>green effect</h1>

  <div class="work-photo two" role="img" aria-label="Photograph of gardeners planting ornamental grasses outside a building"></div>
  <div class="work-photo one" role="img" aria-label="Photograph of a gardener tending fresh plantings in a bed"></div>

  <section class="services">
    <h2 class="services-title">Our Services</h2>
    <div class="services-rule"></div>
    <ul class="services-list">
      <li><svg class="tick" viewBox="0 0 12 12"><circle cx="6" cy="6" r="6" fill="#6cc13a"/><path d="M3.2,6.2 L5.2,8 L8.8,4.2" stroke="#fff" stroke-width="1.6" fill="none"/></svg>Landscape Design &amp; Construction</li>
      <li><svg class="tick" viewBox="0 0 12 12"><circle cx="6" cy="6" r="6" fill="#6cc13a"/><path d="M3.2,6.2 L5.2,8 L8.8,4.2" stroke="#fff" stroke-width="1.6" fill="none"/></svg>Paver Patio/path installations</li>
      <li><svg class="tick" viewBox="0 0 12 12"><circle cx="6" cy="6" r="6" fill="#6cc13a"/><path d="M3.2,6.2 L5.2,8 L8.8,4.2" stroke="#fff" stroke-width="1.6" fill="none"/></svg>Retaining wall installations</li>
      <li><svg class="tick" viewBox="0 0 12 12"><circle cx="6" cy="6" r="6" fill="#6cc13a"/><path d="M3.2,6.2 L5.2,8 L8.8,4.2" stroke="#fff" stroke-width="1.6" fill="none"/></svg>Pergola Installations</li>
      <li><svg class="tick" viewBox="0 0 12 12"><circle cx="6" cy="6" r="6" fill="#6cc13a"/><path d="M3.2,6.2 L5.2,8 L8.8,4.2" stroke="#fff" stroke-width="1.6" fill="none"/></svg>Grading</li>
      <li><svg class="tick" viewBox="0 0 12 12"><circle cx="6" cy="6" r="6" fill="#6cc13a"/><path d="M3.2,6.2 L5.2,8 L8.8,4.2" stroke="#fff" stroke-width="1.6" fill="none"/></svg>All Hardscape construction</li>
      <li><svg class="tick" viewBox="0 0 12 12"><circle cx="6" cy="6" r="6" fill="#6cc13a"/><path d="M3.2,6.2 L5.2,8 L8.8,4.2" stroke="#fff" stroke-width="1.6" fill="none"/></svg>Drainage specialist</li>
      <li><svg class="tick" viewBox="0 0 12 12"><circle cx="6" cy="6" r="6" fill="#6cc13a"/><path d="M3.2,6.2 L5.2,8 L8.8,4.2" stroke="#fff" stroke-width="1.6" fill="none"/></svg>Yard Maintenance plans</li>
      <li><svg class="tick" viewBox="0 0 12 12"><circle cx="6" cy="6" r="6" fill="#6cc13a"/><path d="M3.2,6.2 L5.2,8 L8.8,4.2" stroke="#fff" stroke-width="1.6" fill="none"/></svg>Mulch &amp; Pine needles</li>
      <li><svg class="tick" viewBox="0 0 12 12"><circle cx="6" cy="6" r="6" fill="#6cc13a"/><path d="M3.2,6.2 L5.2,8 L8.8,4.2" stroke="#fff" stroke-width="1.6" fill="none"/></svg>Bloomin' Great Service!</li>
    </ul>
  </section>

  <div class="promise">Dependable Professionals<br>Dedicated to the quality<br>of your Property</div>

  <div class="discount">
    <svg class="discount-star" viewBox="-100 -100 200 200" aria-hidden="true">
      <polygon points="0,-100 28.2,-38.8 95.1,-30.9 45.6,14.8 58.8,80.9 0,48 -58.8,80.9 -45.6,14.8 -95.1,-30.9 -28.2,-38.8" fill="var(--sun)" stroke="#f3f3f3" stroke-width="3" stroke-linejoin="round"/>
    </svg>
    <div class="discount-lead">Mention this flyer for a</div>
    <div class="discount-value">10%</div>
    <div class="discount-label">DISCOUNT!</div>
  </div>

  <div class="contact-tab">CONTACT US</div>

  <div class="contact-line">
    <span class="contact-item phone">
      <svg class="contact-icon" viewBox="0 0 24 24"><path d="M6.6,10.8 C8,13.6 10.4,16 13.2,17.4 L15.4,15.2 C15.7,14.9 16.1,14.8 16.4,14.9 C17.5,15.3 18.7,15.5 20,15.5 C20.6,15.5 21,15.9 21,16.5 V20 C21,20.6 20.6,21 20,21 C10.6,21 3,13.4 3,4 C3,3.4 3.4,3 4,3 H7.5 C8.1,3 8.5,3.4 8.5,4 C8.5,5.3 8.7,6.5 9.1,7.6 C9.2,7.9 9.1,8.3 8.8,8.6 Z" fill="#6cc13a"/></svg>
      7045182094
    </span>
    <span class="contact-item email">
      <svg class="contact-icon" viewBox="0 0 24 24"><rect x="2" y="5" width="20" height="14" rx="2" fill="#6cc13a"/><path d="M3,6 L12,13 L21,6" stroke="#5b3518" stroke-width="2" fill="none"/></svg>
      kestrelgardenworks@mailbox-example.com
    </span>
    <span class="contact-item web">
      <svg class="contact-icon" viewBox="0 0 24 24"><circle cx="12" cy="12" r="10" fill="#6cc13a"/><path d="M2,12 H22 M12,2 C8,6 8,18 12,22 C16,18 16,6 12,2" stroke="#5b3518" stroke-width="1.5" fill="none"/></svg>
      www.kestrelgardenworks-example.com
    </span>
  </div>

</main>
</body>
</html>
```